business card for a massage therapy practice named 'Meadow and Willow Massage Studio'

I really need a trendy, yet easy on the eyes business card to complement my logo. Ideally with some gold or rose gold foil work.

My uploaded file of the logo I have in horizontal but I have a vertical version as well. Another color that is used in the website is a blush pink here and there. I'd like to see some trendy tropical leaves in the design.

```html
<!DOCTYPE html>
<html lang="en">
<head>
<meta charset="utf-8">
<title>Meadow and Willow Massage Studio — Business Card</title>
<link rel="stylesheet" href="https://fonts.googleapis.com/css2?family=Nunito+Sans:wght@300;400;600&display=swap">
<style>
  :root {
    --stage: #efece7;
    --paper: #ffffff;
    --teal: #7ccbb8;
    --teal-deep: #5fb8a3;
    --ink: #2a2a2a;
    --gold: #a8906a;
    --mist: rgba(214, 210, 202, 0.75);
    --mist-clear: rgba(214, 210, 202, 0);
    --olive: rgba(150, 160, 128, 0.85);
    --olive-clear: rgba(150, 160, 128, 0);
    --shadow: rgba(40, 40, 30, 0.18);
  }
  * { box-sizing: border-box; margin: 0; padding: 0; }
  html, body {
    width: 1200px; height: 795px; overflow: hidden;
    background: var(--stage);
    font-family: "Nunito Sans", Arial, sans-serif;
  }
  .stage { position: relative; width: 1200px; height: 795px; }
  .card {
    position: absolute; top: 243px;
    width: 540px; height: 309px;
    overflow: hidden;
    box-shadow: 0 10px 28px var(--shadow);
  }
  .card--info { left: 50px; background: var(--paper); }
  .card--brand { left: 610px; background: var(--teal); }

  .card__band { position: absolute; inset: 0; }

  .illustration { position: absolute; }
  .illustration--corner {
    left: 0; top: 0; width: 230px; height: 180px;
    background: radial-gradient(ellipse at 40% 40%, var(--mist) 0%, var(--mist-clear) 70%);
  }
  .illustration--side {
    left: 370px; top: 80px; width: 170px; height: 170px;
    background: radial-gradient(ellipse at 55% 55%, var(--mist) 0%, var(--mist-clear) 70%);
  }
  .illustration--feature {
    left: 370px; top: 70px; width: 170px; height: 239px;
    background: radial-gradient(ellipse at 55% 60%, var(--olive) 0%, var(--olive-clear) 72%);
  }

  .brandmark {
    position: absolute; display: flex; align-items: center; gap: 10px;
    font-weight: 600; color: var(--ink); line-height: 1.15;
  }
  .brandmark__dot { flex: none; border-radius: 50%; background: var(--gold); }
  .card--info .brandmark { top: 28px; right: 30px; font-size: 14px; }
  .card--info .brandmark__dot { width: 22px; height: 22px; }
  .card--brand .brandmark { top: 118px; left: 80px; font-size: 24px; }
  .card--brand .brandmark__dot { width: 38px; height: 38px; }

  .therapist {
    position: absolute; top: 116px; left: 196px;
    font-size: 18px; font-weight: 300; color: var(--teal-deep);
    letter-spacing: 0.3px;
  }
  .contacts { position: absolute; top: 146px; left: 34px; list-style: none; }
  .contacts__item {
    display: flex; align-items: center; gap: 12px;
    font-size: 14.5px; color: var(--ink); height: 23px;
  }
  .contacts__icon {
    width: 17px; height: 17px; border-radius: 50%;
    background: var(--teal); flex: none;
    display: flex; align-items: center; justify-content: center;
  }
  .website {
    position: absolute; right: 34px; bottom: 22px;
    color: var(--paper); font-size: 14px; letter-spacing: 0.3px;
  }
</style>
</head>
<body>
<main class="stage">

  <section class="card card--info" aria-label="Card front with contact details">
    <div class="illustration illustration--corner" role="img" aria-label="Faint tropical fruit illustration"></div>
    <div class="illustration illustration--side" role="img" aria-label="Faint tropical fruit and leaves illustration"></div>
    <svg class="card__band" width="540" height="309" viewBox="0 0 540 309" aria-hidden="true">
      <path d="M0 262 Q260 255 540 185 L540 309 L0 309 Z" fill="var(--teal)"/>
    </svg>

    <div class="brandmark">
      <span class="brandmark__dot"></span>
      <span>Meadow and Willow<br>Massage Studio</span>
    </div>

    <p class="therapist">Elena Marsh LMT</p>

    <ul class="contacts">
      <li class="contacts__item">
        <span class="contacts__icon">
          <svg width="9" height="9" viewBox="0 0 10 10"><path d="M2 1 L4 1 L4.6 3.2 L3.4 4.2 Q4.4 6 6 6.8 L7 5.6 L9 6.2 L9 8.2 Q5 8.6 2.6 6 Q1 4 2 1 Z" fill="#fff"/></svg>
        </span>555.214.7730
      </li>
      <li class="contacts__item">
        <span class="contacts__icon">
          <svg width="10" height="8" viewBox="0 0 10 8"><rect x="0.6" y="0.6" width="8.8" height="6.8" fill="none" stroke="#fff" stroke-width="1.1"/><path d="M0.6 0.8 L5 4.6 L9.4 0.8" fill="none" stroke="#fff" stroke-width="1.1"/></svg>
        </span>meadowandwillow@mailbox.com
      </li>
      <li class="contacts__item"><span class="contacts__icon"></span>@meadowandwillow</li>
      <li class="contacts__item"><span class="contacts__icon"></span>@meadowandwillow</li>
    </ul>

    <p class="website">www.meadowandwillow.com</p>
  </section>

  <section class="card card--brand" aria-label="Card back with studio name">
    <div class="illustration illustration--feature" role="img" aria-label="Tropical fruit and leaves illustration"></div>

    <div class="brandmark">
      <span class="brandmark__dot"></span>
      <span>Meadow and Willow<br>Massage Studio</span>
    </div>
  </section>

</main>
</body>
</html>
```